Book Cover Design Project

book cover: The Gilded Magpie by Rosalind Partwell

Here's a synopsis of the book: Rita married rich and spent her days disapproving of her stepdaughter, shopping or seeing to it waiters and certain shop girls were fired. It all changed however after she was paid a visit in her palatial home. In her misadventures she makes some acquaintances and foes, but she is always stuck in the same situation. The bridges she has burned and the wrongs she has done have pushed their way into her life. Is she resigned to live the rest of her days like this? Will she roll up her sleeves and do something?

Sample chapter #1: http://velmorpages.example.com/2013/02/08/chapter-1/

This will be an ebook so the illustration should look good as a thumbnail. Here are some covers that will show my tastes:
http://blog.lumistrabeauty.example.co.uk/wp-content/uploads/2010/11/bannerblogblog.png

http://petalpage-reads.example.com/wp-content/uploads/2011/12/odette.jpg

http://www.brambleworthcatalogs.example.com/TR/vlarge/9780000000000_0_Cover.jpg

http://2.img.quillnest.example.com/_QXTokPzmrB/TnFZ8Sv0j6K/AAAAAAAAAKR/7cGx4f_nz-h/s400/corinne+dale+moon+over+tuesday.jpg

The Gilded Magpie is a novella. If you have time, read the first chapter I put in my brief.

Industry/Entity Type

Shopping

Requirements
Must have
• The cover is TIFF (.tif/.tiff) or JPEG (.jpeg/.jpg) format
At least 1000 pixels on the longest side, with an ideal height/width ratio of 1.6.
2500 pixels on the longest side is preferred.
Should not have
• This story is a novella, it is not a novel. So it should not say novel.

```html
<!DOCTYPE html>
<html lang="en">
<head>
<meta charset="utf-8">
<title>The Gilded Magpie — a novella by Rosalind Partwell</title>
<link rel="stylesheet" href="https://fonts.googleapis.com/css2?family=Comfortaa:wght@300&family=Great+Vibes&family=Open+Sans:ital,wght@1,400;1,700&display=swap">
<style>
  :root {
    --page: #ffffff;
    --wine: #561417;
    --wine-mid: #4a1114;
    --wine-deep: #3a0d10;
    --damask: #6e1a1c;
    --ribbon: #0c0c0c;
    --ribbon-line: #1f1f1f;
    --silver: #f4f4f4;
    --silver-shade: #b9b9b9;
    --title-shadow: rgba(30, 4, 6, 0.6);
    --flourish: rgba(235, 235, 235, 0.16);
    --cup-light: #f7f7f7;
    --cup-dark: #c8c8c8;
  }
  html, body {
    margin: 0;
    padding: 0;
    width: 900px;
    height: 1200px;
    overflow: hidden;
    background: var(--page);
  }
  .canvas {
    position: relative;
    width: 900px;
    height: 1200px;
  }
  .cover {
    position: absolute;
    left: 72px;
    top: 0;
    width: 756px;
    height: 1200px;
    overflow: hidden;
  }
  .damask-field {
    position: absolute;
    inset: 0;
    background:
      radial-gradient(circle at 50% 50%, var(--damask) 0 18%, transparent 42%) 0 0 / 126px 150px,
      radial-gradient(ellipse at 50% 45%, var(--wine) 0%, var(--wine-mid) 55%, var(--wine-deep) 100%);
    opacity: 1;
  }
  .byline-band {
    position: absolute;
    left: 72px;
    top: 68px;
    width: 756px;
    height: 92px;
    background:
      repeating-linear-gradient(90deg, var(--ribbon) 0 4px, var(--ribbon-line) 4px 6px),
      var(--ribbon);
    box-shadow: 8px 10px 12px rgba(0, 0, 0, 0.55);
    display: flex;
    align-items: center;
    justify-content: center;
  }
  .byline {
    margin: 0;
    font-family: "Open Sans", Arial, sans-serif;
    font-style: italic;
    font-weight: 400;
    font-size: 25px;
    color: var(--silver);
    letter-spacing: 0.3px;
  }
  .byline .author {
    font-weight: 700;
    font-size: 27px;
  }
  .flourish-field {
    position: absolute;
    left: 100px;
    top: 255px;
    width: 720px;
    height: 620px;
    border-radius: 50% 50% 45% 45%;
    background: radial-gradient(ellipse at 50% 48%, var(--flourish) 0%, rgba(235,235,235,0.07) 45%, transparent 72%);
  }
  .title {
    position: absolute;
    left: 72px;
    top: 430px;
    width: 756px;
    margin: 0;
    color: var(--silver);
    font-weight: 400;
  }
  .title .article {
    position: absolute;
    left: 78px;
    top: 0;
    font-family: "Comfortaa", Arial, sans-serif;
    font-weight: 300;
    font-size: 58px;
    line-height: 1;
    text-shadow: 4px 5px 0 var(--title-shadow);
  }
  .title .name {
    position: absolute;
    left: 0;
    top: 50px;
    width: 756px;
    text-align: center;
    font-family: "Great Vibes", cursive;
    font-size: 128px;
    line-height: 1.4;
    white-space: nowrap;
    background: linear-gradient(180deg, var(--silver) 35%, var(--silver-shade) 100%);
    -webkit-background-clip: text;
    background-clip: text;
    color: transparent;
    filter: drop-shadow(5px 6px 0 var(--title-shadow));
  }
  .cup-art {
    position: absolute;
    left: 398px;
    top: 890px;
    width: 156px;
    height: 245px;
  }
</style>
</head>
<body>
<main class="canvas">
  <section class="cover">
    <div class="damask-field" role="img" aria-label="Deep red damask wallpaper pattern"></div>
  </section>

  <header class="byline-band">
    <p class="byline">a novella by <span class="author">Rosalind Partwell</span></p>
  </header>

  <div class="flourish-field" role="img" aria-label="Silver calligraphic flourishes swirling around the title and rising as steam from the mug"></div>

  <h1 class="title">
    <span class="article">the</span>
    <span class="name">Gilded Magpie</span>
  </h1>

  <svg class="cup-art" viewBox="0 0 156 245" role="img" aria-label="Illustration of a white footed glass mug with a small damask emblem">
    <defs>
      <linearGradient id="cup-tone" x1="0" y1="0" x2="1" y2="0">
        <stop offset="0" stop-color="#f7f7f7"/>
        <stop offset="1" stop-color="#c8c8c8"/>
      </linearGradient>
    </defs>
    <rect x="6" y="8" width="150" height="237" rx="26" fill="rgba(20,3,5,0.35)"/>
    <rect x="0" y="0" width="150" height="237" rx="26" fill="url(#cup-tone)" opacity="0.92"/>
  </svg>
</main>
</body>
</html>
```